" Atendimento personalizado as necessidades do cliente em todos os ramos de tradução. Assistência 24h com plataforma online. Garantindo a segurança de toda documentação pela QTR, Pex, Velkor. "

```html
<!DOCTYPE html>
<html lang="pt-BR">
<head>
<meta charset="utf-8">
<title>Veltrano Traduções – Cartão de visita</title>
<link rel="stylesheet" href="https://fonts.googleapis.com/css2?family=Cinzel:wght@700&family=Montserrat:wght@300;400&display=swap">
<style>
  :root {
    --page-bg: #e9ebee;
    --card-navy: #1f3a5c;
    --accent-blue: #6cc4ef;
    --text-white: #ffffff;
    --text-soft: #c9d6e6;
  }
  * { box-sizing: border-box; margin: 0; padding: 0; }
  html, body {
    width: 1200px;
    height: 1200px;
    overflow: hidden;
    background: var(--page-bg);
  }
  .business-card {
    position: absolute;
    left: 150px;
    top: 343px;
    width: 900px;
    height: 514px;
    background: var(--card-navy);
    color: var(--text-white);
    font-family: "Montserrat", Arial, sans-serif;
  }
  .brand {
    position: absolute;
    top: 78px;
    left: 0;
    width: 100%;
    text-align: center;
  }
  .brand-dot {
    display: block;
    width: 70px;
    height: 70px;
    margin: 0 auto 22px;
    border-radius: 50%;
    background: var(--accent-blue);
  }
  .brand-name {
    font-family: "Cinzel", Georgia, serif;
    font-weight: 700;
    font-size: 74px;
    letter-spacing: 2px;
    line-height: 1;
    color: var(--text-white);
  }
  .brand-tagline {
    margin-top: 8px;
    font-weight: 300;
    font-size: 17px;
    letter-spacing: 14px;
    padding-left: 14px;
    color: var(--text-soft);
  }
  .contact-row {
    position: absolute;
    top: 350px;
    left: 48px;
    right: 48px;
    display: flex;
    justify-content: space-between;
    align-items: flex-start;
    font-size: 14px;
    font-weight: 400;
    color: var(--text-soft);
    line-height: 1.35;
  }
  .contact-item {
    display: flex;
    align-items: flex-start;
    gap: 9px;
  }
  .contact-icon {
    flex: none;
    width: 20px;
    height: 20px;
    border-radius: 50%;
    background: var(--accent-blue);
    display: flex;
    align-items: center;
    justify-content: center;
  }
  .contact-icon svg { width: 12px; height: 12px; }
  .website {
    position: absolute;
    top: 432px;
    width: 100%;
    text-align: center;
    font-size: 22px;
    font-weight: 400;
    letter-spacing: 1px;
    color: var(--text-white);
  }
  .accent-strip {
    position: absolute;
    left: 0;
    bottom: 0;
    width: 100%;
    height: 16px;
    background: var(--accent-blue);
  }
</style>
</head>
<body>
  <section class="business-card">
    <div class="brand">
      <span class="brand-dot"></span>
      <div class="brand-name">VELTRANO</div>
      <div class="brand-tagline">TRADUÇÕES</div>
    </div>

    <div class="contact-row">
      <div class="contact-item">
        <span class="contact-icon">
          <svg viewBox="0 0 24 24"><path fill="#1f3a5c" d="M6.6 10.8a15.1 15.1 0 0 0 6.6 6.6l2.2-2.2c.3-.3.7-.4 1-.2 1.1.4 2.3.6 3.6.6.6 0 1 .4 1 1V20c0 .6-.4 1-1 1A17 17 0 0 1 3 4c0-.6.4-1 1-1h3.5c.6 0 1 .4 1 1 0 1.3.2 2.5.6 3.6.1.3 0 .7-.2 1z"/></svg>
        </span>
        <span>99 9 9999 99 99 | 9999 99 99</span>
      </div>
      <div class="contact-item">
        <span class="contact-icon">
          <svg viewBox="0 0 24 24"><path fill="#1f3a5c" d="M3 5h18v14H3z"/><path fill="none" stroke="#6cc4ef" stroke-width="2" d="M3 6l9 7 9-7"/></svg>
        </span>
        <span>contato@veltrano.com.br</span>
      </div>
      <div class="contact-item">
        <span class="contact-icon">
          <svg viewBox="0 0 24 24"><path fill="#1f3a5c" d="M12 2a7 7 0 0 0-7 7c0 5.2 7 13 7 13s7-7.8 7-13a7 7 0 0 0-7-7zm0 9.5A2.5 2.5 0 1 1 12 6.5a2.5 2.5 0 0 1 0 5z"/></svg>
        </span>
        <span>Rua das Letras, 9999 | Centro<br>Sala 1000 - CEP: 55.555-555<br>Cidade - UF</span>
      </div>
    </div>

    <div class="website">www.veltrano.com.br</div>
    <div class="accent-strip"></div>
  </section>
</body>
</html>
```